Meridale Counsel Corp Business Card design and layout

Meridale Counsel is a small, professional advisory firm specializing in business process consulting and advisory services. We are focused in the energy sector. The business card is to have a combination of blue shades and be professional and serious in nature. Investment banking, capital management, and professional service company card layouts should be used for similar templates

Target Market(s)

Medium to major corporations.

Industry/Entity Type

Consulting

Contact Information for Business Card

The card is to be professional looking in nature and must incorporate the company logo and name in some manner. A two sided design where the opposite side has a QR code and the logo is required.

Logo Text

Lindhaven Holdings Inc.

Colors
0592cd
0455a3
3276b5
33a6d7
85cae6
85abd2
cee9f5
cedeed
ecf7fb

Requirements
Must have
• The card is to be professional and have space for employee, title, address, website, and phone numbers (office and cell). The layout must be some shades of blue.
Nice to have
• A space for embossing and/or some subtle gold highlights
Should not have
• Rainbow colours, unprofessional looking fonts (scribble, cursive writing)

```html
<!DOCTYPE html>
<html lang="en">
<head>
<meta charset="utf-8">
<title>Meridale Counsel Corp – Business Card</title>
<link href="https://fonts.googleapis.com/css2?family=Barlow+Condensed:wght@500;600&family=Roboto:ital,wght@1,400&display=swap" rel="stylesheet">
<style>
  :root {
    --backdrop: #cbcbcb;
    --navy: #15306e;
    --deep-blue: #0455a3;
    --paper: #f7f7f5;
    --sky: #0592cd;
    --light-sky: #33a6d7;
    --white: #ffffff;
  }
  * { margin: 0; padding: 0; box-sizing: border-box; }
  html, body { width: 1200px; height: 1182px; overflow: hidden; background: var(--backdrop); }
  .sheet { position: relative; width: 1200px; height: 1182px; }
  .card { position: absolute; left: 283px; width: 633px; height: 382px; overflow: hidden; }
  .card-front { top: 173px; background: var(--navy); display: flex; align-items: center; justify-content: center; }
  .card-back { top: 626px; background: var(--paper); }
  .brand-name {
    font-family: "Barlow Condensed", sans-serif; font-weight: 600;
    text-transform: uppercase; letter-spacing: 2px; line-height: 1; text-align: center;
  }
  .card-front .brand-name { color: var(--white); font-size: 46px; }
  .card-back .brand-name {
    position: absolute; left: 30px; top: 238px; width: 240px;
    color: var(--navy); font-size: 34px;
  }
  .header-band {
    position: absolute; left: 0; top: 0; width: 633px; height: 118px;
    background: linear-gradient(180deg, var(--navy) 0%, var(--navy) 70%, var(--deep-blue) 100%);
  }
  .holder { position: absolute; right: 30px; top: 32px; text-align: right; color: var(--white); }
  .holder-name { font-family: "Barlow Condensed", sans-serif; font-weight: 600; font-size: 24px; line-height: 1.1; }
  .holder-title { font-family: "Roboto", sans-serif; font-style: italic; font-size: 13.5px; }
  .contacts { position: absolute; right: 30px; top: 247px; list-style: none;
    font-family: "Barlow Condensed", sans-serif; font-weight: 500; font-size: 15px; color: var(--navy); }
  .contacts li { display: flex; justify-content: flex-end; align-items: center; gap: 5px; height: 20px; }
  .contacts .accent { color: var(--light-sky); }
  .contacts .address { margin-top: 7px; }
  .contacts svg { width: 14px; height: 12px; fill: var(--light-sky); }
</style>
</head>
<body>
<main class="sheet">
  <section class="card card-front">
    <p class="brand-name">Meridale<br>Counsel Corp</p>
  </section>

  <section class="card card-back">
    <div class="header-band" role="img" aria-label="Decorative navy header band"></div>
    <div class="holder">
      <p class="holder-name">Daniel Marchetti, P.Eng</p>
      <p class="holder-title">President</p>
    </div>
    <p class="brand-name">Meridale<br>Counsel Corp</p>
    <ul class="contacts">
      <li>403-555-0182
        <svg viewBox="0 0 14 12"><path d="M1,4 C1,1 13,1 13,4 L10,5 L9,3 H5 L4,5 Z M3,6 H11 L12,11 H2 Z"/></svg></li>
      <li><span>www.<span class="accent">meridalecounselcorp</span>.com</span>
        <svg viewBox="0 0 14 12"><path d="M1,2 H13 V10 H1 Z M2,3 L7,7 L12,3" stroke="#fff" stroke-width="0.8"/></svg></li>
      <li>dmarchetti@meridalecounselcorp.com
        <svg viewBox="0 0 14 12"><circle cx="7" cy="6" r="5.5"/><path d="M1.5,6 H12.5 M7,0.5 V11.5 M3,3 H11 M3,9 H11" stroke="#fff" stroke-width="0.7" fill="none"/></svg></li>
      <li class="address">310, 814- 9th Ave, SW Calgary, AB T2P 1K4</li>
    </ul>
  </section>
</main>
</body>
</html>
```